Personal Training

Personal Fitness Trainer
Sports Nutritionist
Individual and Group rates available
Certifications
Global Wellness Coaches Federation
Worldwide Athletic Study Council

Industry/Entity Type

Fitness

Contact Information for Business Card

Dorinda Valcourt
555-284-7160
dvalcourt4@brimfeld.com

```html
<!DOCTYPE html>
<html lang="en">
<head>
<meta charset="utf-8">
<title>Dorinda Valcourt – Personal Training Business Card</title>
<link href="https://fonts.googleapis.com/css2?family=Questrial&family=Quicksand:wght@500;600&family=Parisienne&display=swap" rel="stylesheet">
<style>
  :root {
    --backdrop: #e9e6e2;
    --card-white: #ffffff;
    --purple: #9a73c0;
    --purple-deep: #7d56a6;
    --purple-light: #c4aedb;
    --ink: #222222;
    --silver-light: #d6d6d8;
    --silver-mid: #a9a9ad;
    --silver-dark: #8a8a8f;
    --photo-tone-a: #8f83a6;
    --photo-tone-b: #4f4566;
    --badge-red: #d8443b;
    --badge-blue: #3a4f9c;
    --badge-grey: #6b6b6b;
  }
  * { box-sizing: border-box; margin: 0; padding: 0; }
  html, body { width: 1200px; height: 1000px; overflow: hidden; }
  body { background: var(--backdrop); position: relative; font-family: "Questrial", sans-serif; }

  .card { position: absolute; overflow: hidden; box-shadow: 0 10px 24px rgba(0,0,0,.18); }

  /* Back card */
  .card-back { left: 50px; top: 200px; width: 640px; height: 366px; background: var(--card-white); }
  .card-back .gym-photo {
    position: absolute; left: 0; top: 0; width: 210px; height: 100%;
    background: linear-gradient(160deg, var(--photo-tone-a), var(--photo-tone-b));
  }
  .card-back .rates {
    position: absolute; left: 240px; top: 34px; width: 380px;
    font-family: "Quicksand", sans-serif; font-weight: 600;
    color: var(--purple); font-size: 34px; line-height: 1.2;
  }
  .card-back .cert-band {
    position: absolute; left: 210px; top: 150px; right: 0; height: 46px;
    background: linear-gradient(90deg, var(--purple-light), var(--purple) 30%, var(--purple-deep));
    color: #fff; font-family: "Quicksand", sans-serif; font-weight: 500;
    font-size: 26px; line-height: 46px; padding-left: 40px;
  }
  .card-back .cert-list {
    position: absolute; left: 240px; top: 214px;
    font-size: 15px; color: var(--ink); line-height: 1.45; list-style: none;
  }
  .card-back .badges { position: absolute; left: 250px; top: 272px; display: flex; gap: 46px; align-items: center; }

  /* Front card */
  .card-front {
    left: 770px; top: 140px; width: 380px; height: 665px;
    background:
      repeating-linear-gradient(90deg, rgba(255,255,255,.08) 0 1px, rgba(0,0,0,.04) 1px 3px),
      linear-gradient(180deg, var(--silver-light), var(--silver-mid) 55%, var(--silver-dark));
  }
  .card-front .name-arc { position: absolute; left: 0; top: 0; width: 380px; height: 120px; }
  .card-front .name {
    position: absolute; left: 0; top: 26px; width: 100%; text-align: center;
    font-family: "Parisienne", cursive; font-size: 46px; color: #fff;
  }
  .card-front .trainer-photo {
    position: absolute; left: 0; top: 120px; width: 190px; height: 545px;
    background: linear-gradient(180deg, #b08b78, #8c5e52 40%, #3a3a44 70%, #2a2a30);
  }
  .card-front .roles {
    position: absolute; left: 180px; top: 150px; width: 190px; text-align: center;
    color: #fff; font-size: 30px; line-height: 1.18; text-shadow: 0 1px 2px rgba(0,0,0,.35);
  }
  .card-front .roles p + p { margin-top: 34px; }
  .card-front .contact {
    position: absolute; right: 18px; bottom: 26px; text-align: right;
    color: #fff; font-size: 19px; line-height: 1.7; text-shadow: 0 1px 2px rgba(0,0,0,.35);
  }
</style>
</head>
<body>

<section class="card card-back">
  <div class="gym-photo" role="img" aria-label="Photo of a trainer lifting in a gym, purple-toned black and white"></div>
  <h2 class="rates">Individual and Group rates available</h2>
  <div class="cert-band">Certifications</div>
  <ul class="cert-list">
    <li>Global Wellness Coaches Federation</li>
    <li>Worldwide Athletic Study Council</li>
  </ul>
  <div class="badges">
    <svg width="60" height="60" viewBox="0 0 60 60" aria-hidden="true"><circle cx="30" cy="30" r="26" fill="var(--badge-grey)"/></svg>
    <svg width="120" height="56" viewBox="0 0 120 56" aria-hidden="true"><rect x="4" y="4" width="112" height="48" fill="var(--badge-blue)"/></svg>
  </div>
</section>

<section class="card card-front">
  <svg class="name-arc" viewBox="0 0 380 120" aria-hidden="true">
    <path d="M0 0 H380 V70 Q190 118 0 102 Z" fill="var(--purple)"/>
    <path d="M0 102 Q190 118 380 70 V78 Q190 126 0 110 Z" fill="var(--purple-light)"/>
  </svg>
  <h1 class="name">Dorinda Valcourt</h1>
  <div class="trainer-photo" role="img" aria-label="Photo of the trainer posing in athletic wear"></div>
  <div class="roles">
    <p>Personal Fitness Trainer</p>
    <p>Sports Nutritionist</p>
  </div>
  <div class="contact">
    <p>555-284-7160</p>
    <p>dvalcourt4@brimfeld.com</p>
  </div>
</section>

</body>
</html>
```